FR banner

we need a banner design (36"x120" horizontal) that will be displayed on a local high school baseball field. My company ( Crestwell Prints Co) has been producing signage for the Fernmoor Ridge community since 2009. We would like to communicate that we do more than banners. The final design should include the slogan "Signs Shirts Swag" and our Logo.

Target Market(s)

companies, teams, events, shirt and other marketing items.

Industry/Entity Type

Sign, Print,

Font styles to use
Sans Serif

Requirements
Should not have
• no baseball content.

```html
<!DOCTYPE html>
<html lang="en">
<head>
<meta charset="UTF-8">
<title>Fernmoor Ridge Field Banner – Crestwell Prints Co</title>
<link rel="stylesheet" href="https://fonts.googleapis.com/css2?family=Russo+One&display=swap">
<style>
  :root {
    --stage-grey: #8d8d8d;
    --ink: #0a0a0a;
    --dye-violet: #7674c8;
    --dye-blue: #8fa8dc;
    --dye-sky: #c3d8f3;
    --dye-white: #ffffff;
  }
  html, body {
    margin: 0;
    padding: 0;
    width: 1200px;
    height: 1200px;
    overflow: hidden;
    background: var(--stage-grey);
  }
  .canvas {
    position: relative;
    width: 1200px;
    height: 1200px;
    background: var(--stage-grey);
  }
  .banner {
    position: absolute;
    left: 67px;
    top: 438px;
    width: 1067px;
    height: 319px;
    overflow: hidden;
  }
  .banner__dye {
    position: absolute;
    inset: 0;
    background:
      radial-gradient(ellipse 38% 70% at 50% 45%, var(--dye-white) 40%, rgba(255,255,255,0) 100%),
      linear-gradient(90deg,
        var(--dye-violet) 0%,
        var(--dye-blue) 6%,
        var(--dye-sky) 14%,
        var(--dye-white) 30%,
        var(--dye-white) 70%,
        var(--dye-sky) 86%,
        var(--dye-blue) 94%,
        var(--dye-violet) 100%);
  }
  .banner__content {
    position: absolute;
    inset: 0;
    display: flex;
    flex-direction: column;
    align-items: center;
  }
  .brand-name {
    margin-top: 62px;
    font-family: "Russo One", sans-serif;
    font-size: 22px;
    color: var(--ink);
    letter-spacing: 0.5px;
    line-height: 1;
  }
  .slogan {
    margin: 20px 0 0;
    font-family: "Russo One", sans-serif;
    font-weight: 400;
    font-size: 92px;
    line-height: 100px;
    color: var(--ink);
    text-align: center;
    letter-spacing: 6px;
    transform: skewX(-8deg);
  }
  .slogan__line { display: block; }
</style>
</head>
<body>
  <main class="canvas">
    <section class="banner">
      <div class="banner__dye" role="img" aria-label="Tie-dye background in violet and sky blue fading to white at the centre"></div>
      <div class="banner__content">
        <div class="brand-name">Crestwell Prints Co</div>
        <h1 class="slogan">
          <span class="slogan__line">SIGNS SHIRTS</span>
          <span class="slogan__line">SWAG</span>
        </h1>
      </div>
    </section>
  </main>
</body>
</html>
```